Brightway Elderplan (03)

We're designing a website to sell Medicare Supplements. Attached is the script we want to say and general layout, but please use your best knowledge to make it better. This platform should be extremely user-friendly, but we want to make it look fun and approachable! Most Insurance/medicare websites are very boring, drab, simple but we want this one to be more personalized, fun and sexy (but again, still user-friendly since our target demographic is 65+).

This homepage should include a fun and inviting quiz, the script is in the attachment below. It should also include the blurbs about what medicare supplements plans are and why they should buy them. Feel free to play around with cool fonts and imagery, we want the site to be engaging!

Target Market(s)

seniors

Industry/Entity Type

Insurance

Number of Pages Required

1 page

Requirements
Must have
• Quiz, company name and tag line, script
Nice to have
• fun, engaging elements

```html
<!DOCTYPE html>
<html lang="en">
<head>
<meta charset="utf-8">
<title>Brightway Elderplan — Medicare Supplement Plans</title>
<link rel="stylesheet" href="https://fonts.googleapis.com/css2?family=Poppins:wght@400;500;600&display=swap">
<style>
:root{
  --teal:#1b9a83;
  --teal-dark:#137563;
  --teal-bright:#22bca3;
  --teal-blob:#188f79;
  --mint:#3fe3bb;
  --ink:#232323;
  --charcoal:#262626;
  --orange:#f59a2c;
  --white:#ffffff;
  --text:#2e2e2e;
  --heading-teal:#1f8f7c;
}
*{box-sizing:border-box;margin:0;padding:0}
html,body{width:1200px;height:2658px;overflow:hidden}
body{font-family:'Poppins',sans-serif;background:var(--white);color:var(--text);position:relative}

/* Header & footer bar */
.bar{position:absolute;left:0;width:1200px;height:104px;background:var(--teal);overflow:hidden}
.bar--top{top:0}
.bar--bottom{top:2554px}
.bar__panel{position:absolute;top:0;right:0;height:104px;width:350px;background:var(--teal-dark);clip-path:polygon(28px 0,100% 0,100% 100%,0 100%)}
.bar__brand{position:absolute;left:40px;top:22px}
.bar__name{font-size:28px;font-weight:500;color:var(--mint);text-transform:uppercase;letter-spacing:.2px;line-height:1.1}
.bar__tagline{font-size:16px;color:var(--white);margin-top:2px}
.bar__call{position:absolute;right:37px;top:22px;text-align:right;color:var(--white);font-size:22px;line-height:28px}
.bar__call strong{font-weight:500}

/* Hero */
.hero{position:absolute;top:104px;left:0;width:1200px;height:546px;background:linear-gradient(120deg,#f1edf0 0%,#d9d2cf 40%,#bdb6b3 65%,#ebe7ea 100%)}
.hero__panel{position:absolute;left:159px;top:135px;width:882px;height:258px;background:rgba(58,58,58,.92);display:flex;align-items:center}
.hero__headline{width:434px;text-align:right;padding-right:32px;font-size:46px;line-height:54px;font-weight:500;color:var(--mint);text-transform:uppercase}
.hero__divider{width:1px;height:158px;background:var(--white)}
.hero__copy{padding-left:23px;width:400px;font-size:24px;line-height:27px;color:var(--white)}
.hero__copy em{font-style:normal;color:var(--mint)}

/* Quiz */
.quiz{position:absolute;left:197px;top:698px;width:806px;height:412px;background:var(--teal-bright);overflow:hidden}
.quiz__blob{position:absolute;left:0;top:0}
.quiz__intro{position:absolute;left:38px;top:54px;color:var(--white)}
.quiz__title{font-size:49px;line-height:54px;font-weight:500}
.quiz__lead{margin-top:20px;font-size:23px;line-height:27px;width:350px}
.quiz__lead b{font-weight:600}
.quiz__form{position:absolute;left:450px;top:26px;color:var(--white);font-size:16px;line-height:20.3px}
.quiz__q{font-weight:500}
.quiz__opt{display:flex;align-items:center;padding-left:14px}
.quiz__radio{width:15px;height:15px;border-radius:50%;background:var(--white);margin-right:6px;position:relative}
.quiz__radio--on::after{content:"";position:absolute;left:4px;top:4px;width:7px;height:7px;border-radius:50%;background:var(--ink)}
.quiz__zip{display:block;margin:7px 0 0 14px;width:185px;height:32px;background:var(--white);border:0}
.quiz__submit{display:block;margin:9px 0 0 14px;width:186px;height:41px;background:var(--orange);color:var(--white);border:0;font:500 16px 'Poppins',sans-serif}

/* About */
.about{position:absolute;left:0;top:1282px;width:1200px;height:550px;background:var(--charcoal)}
.about__text{position:absolute;left:84px;top:46px;width:560px;color:var(--white)}
.about__title{font-size:35px;line-height:40px;font-weight:500;color:var(--mint)}
.about__lead{margin-top:20px;font-size:23px;line-height:27px;font-weight:500}
.about__body{margin-top:19px;font-size:16.5px;line-height:20.5px}
.list{list-style:none;margin-top:19px;font-size:16.5px;line-height:20.5px}
.list li{padding-left:12px;position:relative}
.list li::before{content:"-";position:absolute;left:0}
.about__photo{position:absolute;left:681px;top:0;width:519px;height:550px;background:linear-gradient(160deg,#6e7a4a 0%,#8ea04f 45%,#c4b49d 70%,#7a8b3d 100%)}

/* Costs */
.costs{position:absolute;left:0;top:1832px;width:1200px;height:722px}
.costs__text{position:absolute;left:105px;top:50px;width:610px}
.costs__title{font-size:35px;line-height:40px;font-weight:500;color:var(--heading-teal)}
.costs__lead{margin-top:22px;font-size:23px;line-height:27px;font-weight:500;color:var(--ink)}
.costs__body{margin-top:19px;font-size:16.5px;line-height:20.5px}
.costs .list{margin-top:20px}
.costs__note{margin-top:20px;font-size:16.5px;line-height:20.5px}
.costs__art{position:absolute;left:758px;top:124px;width:362px;height:387px;background:radial-gradient(ellipse at center,#e6eefc 0%,#f4f7fd 55%,#ffffff 80%)}
</style>
</head>
<body>

<header class="bar bar--top">
  <div class="bar__panel"></div>
  <div class="bar__brand">
    <div class="bar__name">Brightway Elderplan</div>
    <div class="bar__tagline">Be confident in choosing the Medicare Supplement plan that’s right for you.</div>
  </div>
  <div class="bar__call">Call <strong>(800) 555-0142</strong><br>to talk to a live agent</div>
</header>

<section class="hero" role="img" aria-label="Photo of a smiling senior couple relaxing together in bed">
  <div class="hero__panel">
    <h1 class="hero__headline">We know insurance can be confusing</h1>
    <div class="hero__divider"></div>
    <p class="hero__copy">With so much information and not enough answers, <em>we’re here to help you find the plan that works best for you,</em> your family and your health.</p>
  </div>
</section>

<section class="quiz">
  <svg class="quiz__blob" width="420" height="412" viewBox="0 0 420 412">
    <path d="M0 0H390C420 70 410 200 340 290C280 370 160 395 70 385C40 382 15 375 0 370Z" fill="#2ab09a"/>
    <path d="M0 0H365C400 80 390 190 320 260C260 330 150 360 60 355C35 354 15 350 0 345Z" fill="var(--teal-blob)"/>
  </svg>
  <div class="quiz__intro">
    <h2 class="quiz__title">Take this<br>short quiz</h2>
    <p class="quiz__lead">to find <b>flexible</b> and <b>affordable plans</b> that you can feel confident in</p>
  </div>
  <form class="quiz__form">
    <div class="quiz__q">1. I am</div>
    <div class="quiz__opt"><span class="quiz__radio quiz__radio--on"></span>Over 64 years old</div>
    <div class="quiz__opt"><span class="quiz__radio"></span>64 years old</div>
    <div class="quiz__opt"><span class="quiz__radio"></span>Under 64 years old</div>
    <div class="quiz__q">2. I am</div>
    <div class="quiz__opt"><span class="quiz__radio quiz__radio--on"></span>Male</div>
    <div class="quiz__opt"><span class="quiz__radio"></span>Female</div>
    <div class="quiz__opt"><span class="quiz__radio"></span>Unspecified</div>
    <div class="quiz__q">3. I want to see</div>
    <div class="quiz__opt"><span class="quiz__radio quiz__radio--on"></span>Free plans</div>
    <div class="quiz__opt"><span class="quiz__radio"></span>Premium plans</div>
    <div class="quiz__opt"><span class="quiz__radio"></span>All plans</div>
    <div class="quiz__q">4. My zip code</div>
    <input class="quiz__zip" type="text" aria-label="Zip code">
    <button class="quiz__submit" type="button">SUBMIT</button>
  </form>
</section>

<section class="about">
  <div class="about__text">
    <h2 class="about__title">What is a Medicare<br>Supplement plan?</h2>
    <p class="about__lead">Each Medicare Supplement insurance plan offers a different level of basic benefits, but each lettered plan will include the same standardized basic benefits regardless of insurance company and location.</p>
    <p class="about__body">Medicare Supplement insurance plans do not always cover vision, dental, long-term care, or hearing aids, but all plans must cover at least a portion of the following basic benefits:</p>
    <ul class="list">
      <li>Medicare Part A coinsurance costs up to an additional<br>365 days after Medicare benefits are exhausted</li>
      <li>Medicare Part A hospice care coinsurance or copayments</li>
      <li>Medicare Part B coinsurance or copayments</li>
      <li>First three pints of blood used in a medical procedure</li>
    </ul>
  </div>
  <div class="about__photo" role="img" aria-label="Photo of a smiling senior man stretching outdoors on the grass"></div>
</section>

<section class="costs">
  <div class="costs__text">
    <h2 class="costs__title">Medicare Supplement<br>insurance plan costs</h2>
    <p class="costs__lead">Although private insurance companies are required to offer the same basic benefits for each lettered plan, they do have the ability to charge different premiums.</p>
    <p class="costs__body">You might want to shop around to find a Medicare Supplement<br>insurance plan that may fit your medical and financial needs.<br>Insurance companies may price their plan premiums in any of<br>the following ways:</p>
    <ul class="list">
      <li>Community no-age-rated : These Medicare Supplement insurance plans charge premiums that are the same across the board, regardless of age.</li>
      <li>Issue-age-rated : These plans base their premiums on your age when you first enrolled in the policy. Therefore, the younger you are when you enroll in this type of plan, the lower your premium will be.</li>
      <li>Attained-age-rated : Like issue-age-rated, these plans base their premiums on the age you were when you first bought a policy, but unlike issue-age-rated, premiums increase as you get older.</li>
    </ul>
    <p class="costs__note">Please note that no matter what rating method an insurance company uses, premiums may increase over time for reasons other than age, such as inflation.</p>
  </div>
  <div class="costs__art" role="img" aria-label="Isometric illustration of medical staff reviewing a large online plan comparison screen"></div>
</section>

<footer class="bar bar--bottom">
  <div class="bar__panel"></div>
  <div class="bar__brand">
    <div class="bar__name">Brightway Elderplan</div>
    <div class="bar__tagline">Be confident in choosing the Medicare Supplement plan that’s right for you.</div>
  </div>
  <div class="bar__call">Call <strong>(800) 555-0142</strong><br>to talk to a live agent</div>
</footer>

</body>
</html>
```